Business Card Design Project - Harbourline Removals

I need a business card design created for my furniture removal business. The name is Harbourline Removals so something associated with the galaxy would be great ( possibly the southern cross or something to that effect). Modern, creative and simple was what I had in mind. I like metallic silver and different shades of blue but am open to other colour ideas.

Industry/Entity Type

Business

Requirements
Must have
• Something associated with the galaxy
Nice to have
• Have checked out lots of different fontstyles and really like 'kefa'

```html
<!DOCTYPE html>
<html lang="en">
<head>
<meta charset="utf-8">
<title>Harbourline Removals – Business Card</title>
<link rel="stylesheet" href="https://fonts.googleapis.com/css2?family=Nunito:wght@600;700;800&display=swap">
<style>
  :root {
    --space-deep: #02141d;
    --space-mid: #0b4a5e;
    --space-teal: #14708a;
    --glow-cyan: #2fd3ff;
    --glow-core: #e8fbff;
    --star-white: #ffffff;
    --star-halo: #bfefff;
    --ink-white: #ffffff;
    --ink-outline: #0a0a0a;
    --tagline-blue: #0b5fae;
    --sofa-light: #ffc21a;
    --sofa-mid: #f0a000;
    --sofa-dark: #a85f00;
  }
  html, body {
    margin: 0;
    padding: 0;
    width: 1200px;
    height: 686px;
    overflow: hidden;
    background: var(--space-deep);
  }
  .business-card {
    display: block;
    width: 1200px;
    height: 686px;
  }
  .card-text {
    font-family: "Nunito", sans-serif;
    text-anchor: middle;
    paint-order: stroke fill;
    stroke-linejoin: round;
  }
  .company-name {
    font-size: 90px;
    font-weight: 700;
    fill: var(--ink-white);
    stroke: var(--ink-outline);
    stroke-width: 5px;
  }
  .company-name-shadow {
    font-size: 90px;
    font-weight: 700;
    fill: rgba(0, 0, 0, 0.5);
    filter: blur(6px);
  }
  .tagline {
    font-size: 52px;
    font-weight: 800;
    fill: var(--tagline-blue);
    stroke: #06243d;
    stroke-width: 3px;
  }
  .contact-line {
    font-size: 49px;
    font-weight: 700;
    fill: var(--ink-white);
    stroke: var(--ink-outline);
    stroke-width: 4px;
  }
  .star-sparkle { fill: var(--star-white); }
  .star-halo { fill: var(--star-halo); opacity: 0.35; }
</style>
</head>
<body>
<svg class="business-card" viewBox="0 0 1200 686" xmlns="http://www.w3.org/2000/svg">
  <defs>
    <radialGradient id="space-backdrop" cx="0.55" cy="0.46" r="0.75">
      <stop offset="0" stop-color="var(--space-teal)"/>
      <stop offset="0.55" stop-color="var(--space-mid)"/>
      <stop offset="1" stop-color="var(--space-deep)"/>
    </radialGradient>
    <radialGradient id="nebula-glow" cx="0.5" cy="0.5" r="0.5">
      <stop offset="0" stop-color="var(--glow-core)"/>
      <stop offset="0.35" stop-color="var(--glow-cyan)" stop-opacity="0.85"/>
      <stop offset="1" stop-color="var(--glow-cyan)" stop-opacity="0"/>
    </radialGradient>
    <linearGradient id="sofa-tones" x1="0" y1="0" x2="0.3" y2="1">
      <stop offset="0" stop-color="var(--sofa-light)"/>
      <stop offset="0.6" stop-color="var(--sofa-mid)"/>
      <stop offset="1" stop-color="var(--sofa-dark)"/>
    </linearGradient>
    <symbol id="sparkle" viewBox="-12 -12 24 24" overflow="visible">
      <circle class="star-halo" r="4"/>
      <path class="star-sparkle" d="M0 -12 L1.2 -1.2 L12 0 L1.2 1.2 L0 12 L-1.2 1.2 L-12 0 L-1.2 -1.2 Z"/>
    </symbol>
  </defs>

  <rect class="space-backdrop" width="1200" height="686" fill="url(#space-backdrop)"/>
  <ellipse class="nebula-glow" cx="640" cy="330" rx="400" ry="210" fill="url(#nebula-glow)"/>

  <g class="starfield">
    <use href="#sparkle" x="345" y="82" width="24" height="24"/>
    <use href="#sparkle" x="443" y="95" width="12" height="12"/>
    <use href="#sparkle" x="801" y="115" width="12" height="12"/>
    <use href="#sparkle" x="669" y="169" width="22" height="22"/>
    <use href="#sparkle" x="1100" y="54" width="14" height="14"/>
    <use href="#sparkle" x="992" y="161" width="24" height="24"/>
    <use href="#sparkle" x="551" y="190" width="10" height="10"/>
    <use href="#sparkle" x="134" y="312" width="12" height="12"/>
    <use href="#sparkle" x="974" y="317" width="12" height="12"/>
    <use href="#sparkle" x="789" y="543" width="12" height="12"/>
    <use href="#sparkle" x="1041" y="569" width="22" height="22"/>
    <use href="#sparkle" x="1026" y="614" width="12" height="12"/>
    <use href="#sparkle" x="443" y="626" width="20" height="20"/>
    <use href="#sparkle" x="337" y="640" width="10" height="10"/>
    <use href="#sparkle" x="1170" y="430" width="10" height="10"/>
  </g>

  <path class="sofa-illustration" role="img" aria-label="Illustration of an orange three-seat sofa floating in space"
        d="M10 470 Q120 380 300 360 Q390 350 410 390 L415 520 Q300 560 150 620 Q60 640 20 620 Z"
        fill="url(#sofa-tones)"/>

  <text class="card-text company-name-shadow" x="612" y="220">Harbourline Removals</text>
  <text class="card-text company-name" x="600" y="258">Harbourline Removals</text>
  <text class="card-text tagline" x="592" y="338">Furniture moving company</text>
  <text class="card-text contact-line" x="600" y="410">Phone: (555) 555 - 555</text>
  <text class="card-text contact-line" x="600" y="480">Email: HarbourlineRemovals@starpost.com</text>
</svg>
</body>
</html>
```